8" x 11" One Page Flyer for Fence Installation Company

We are looking to promote our business with a new flyer that would be handed out in person to people or put at their mailbox/door at their homes. The flyer needs to be creative and attention-grabbing. I have attached some of our previous flyers and our website information. Do not call or email regarding the flyer. We want the flyer to look professional but also friendly. One page, NOT folded. You can use images from our website at www.MyBraxtonYard.com or our Facebook page at www.Facebook.com/HollowbrookRailsBKT. We are flexible with what photos you can use but there must be photos of OUR fences on the flyer. More photos specifically can also be provided. Colors need to be suitable for a flyer printed on canary yellow in color paper OR white paper.

Target Market(s)

Homeowners that need a new fence

Industry/Entity Type

Construction

Font styles to use
Sans Serif
Other font styles liked:
• HD Colton

Colors
0054AA
0677BA
7BADD7
CADEEF
E8F1F8
0094D4
00A9DD
6FCCEA
C7EBF8
E9F6FB

Requirements
Must have
• Our fence photos - mostly wood fence photos (different designs), SIZE SHOULD BE LETTER SIZE 8" x 11"
Nice to have
• A nice bible verse featured at the bottom of the flyer.
Should not have
• DO NOT COPY THE WEBSITE FORMAT, I WANT SOMETHING UNIQUE. Other people's fence photos, they must all come from our website or facebook page

```html
<!DOCTYPE html>
<html lang="en">
<head>
<meta charset="utf-8">
<title>Hollowbrook Rails Flyer</title>
<link href="https://fonts.googleapis.com/css2?family=Montserrat:wght@500;700;800&family=Open+Sans:wght@400;600&display=swap" rel="stylesheet">
<style>
  :root{
    --blue:#0a78d6;
    --blue-dark:#0054aa;
    --ink:#1d1d1d;
    --band:#222222;
    --paper:#ffffff;
    --stage:#ececec;
    --muted:#4a4a4a;
    --wood-light:#d9bf8e;
  }
  *{box-sizing:border-box;margin:0;padding:0}
  html,body{width:1200px;height:909px;overflow:hidden;background:var(--stage)}
  body{font-family:"Open Sans",sans-serif;color:var(--ink)}
  .flyer{position:absolute;left:260px;top:14px;width:680px;height:880px;background:var(--paper);overflow:hidden;box-shadow:0 6px 24px rgba(0,0,0,.18)}
  .backdrop{position:absolute;left:0;top:420px;width:680px;height:460px;background:linear-gradient(160deg,#e4e4e4,#f3f3f3 55%,#dcdcdc)}
  .showroom-band{position:absolute;left:0;top:0;width:680px;height:110px}
  .showroom{position:absolute;left:345px;top:16px;width:320px;color:#fff}
  .showroom h3{font:700 13px "Open Sans",sans-serif;letter-spacing:.2px;margin-bottom:4px}
  .showroom p{font-size:10.5px;line-height:1.45}
  .clock{position:absolute;left:290px;top:28px;width:36px;height:36px}
  .brand{position:absolute;left:24px;top:118px;display:flex;align-items:center;gap:10px}
  .brand-mark{width:44px;height:44px;background:var(--blue-dark)}
  .brand-name{font:700 19px "Montserrat",sans-serif;color:var(--blue)}
  .brand-phone{font:800 18px "Montserrat",sans-serif;color:var(--ink);line-height:1}
  .brand-tag{font-size:7.5px;color:var(--ink);margin-top:2px}
  .intro{position:absolute;left:0;top:175px;width:430px;height:285px}
  .intro-text{position:absolute;left:40px;top:210px;width:310px;color:#fff}
  .intro-text h1{font:800 24px "Montserrat",sans-serif;letter-spacing:.5px}
  .intro-text h2{font:700 17px "Montserrat",sans-serif;line-height:1.35;margin:8px 0 14px}
  .intro-text p{font-size:12px;line-height:1.6}
  .photo{position:absolute;border:4px solid #fff}
  .photo-main{left:380px;top:110px;width:300px;height:250px;background:linear-gradient(170deg,#4d7a3a,#8fa45c 40%,var(--wood-light) 75%,#c9a770)}
  .photo-rail{left:510px;top:355px;width:160px;height:135px;background:linear-gradient(160deg,#3f6b34,#7d8f55 55%,#c9ad7a)}
  .photo-metal{left:300px;top:395px;width:200px;height:135px;background:linear-gradient(170deg,#b9c4cc,#7b8a5a 45%,#4a4a40 75%,#8a6a4a)}
  .photo-post{left:50px;top:428px;width:220px;height:132px;background:linear-gradient(150deg,#6fa3d8,#3f6b34 35%,#b89558 70%,#8f7048)}
  .why{position:absolute;left:50px;top:572px;width:300px}
  .why h2,.contact h2{font:800 24px "Montserrat",sans-serif;color:var(--ink);line-height:1.2}
  .why h2 span,.contact h2 span{color:var(--blue)}
  .why .lead{font-size:13.5px;line-height:1.35;margin:6px 0 6px;color:var(--ink)}
  .why ul{list-style:none}
  .why li{display:flex;align-items:center;gap:8px;font-size:11.5px;color:var(--muted);line-height:1.5}
  .why li svg{width:10px;height:10px;flex:none}
  .divider{position:absolute;left:355px;top:560px;width:1px;height:210px;background:#b9b9b9}
  .contact{position:absolute;left:380px;top:545px;width:290px}
  .contact ul{list-style:none;margin-top:14px}
  .contact li{display:flex;align-items:center;gap:14px;font:600 11.5px "Montserrat",sans-serif;margin-bottom:10px}
  .contact li svg{width:36px;height:36px;flex:none}
  .footer{position:absolute;left:0;top:800px;width:680px;height:80px;background:var(--blue);color:#fff;text-align:center;padding-top:16px}
  .footer .verse{font:800 20px "Montserrat",sans-serif;letter-spacing:.6px}
  .footer .ref{font:500 13px "Montserrat",sans-serif;margin-top:4px;letter-spacing:.5px}
</style>
</head>
<body>
<main class="flyer">
  <div class="backdrop" role="img" aria-label="Faded photo of a wood rail fence with wire mesh"></div>

  <svg class="showroom-band" viewBox="0 0 680 110" aria-hidden="true">
    <polygon points="260,0 680,0 680,88 360,88 300,110 275,88" fill="var(--band)"/>
  </svg>
  <svg class="clock" viewBox="0 0 36 36" aria-hidden="true">
    <circle cx="18" cy="18" r="17" fill="#fff"/>
    <circle cx="18" cy="18" r="7" fill="none" stroke="var(--blue)" stroke-width="2"/>
    <path d="M18 14v4h3" fill="none" stroke="var(--blue)" stroke-width="2" stroke-linecap="round"/>
  </svg>
  <div class="showroom">
    <h3>VISIT OUR SHOWROOM:</h3>
    <p>Our outdoor showroom is open 24/7, while our indoor showroom &amp; office is open Monday - Thurs 9AM - 3PM, Friday 9AM - 1PM</p>
  </div>

  <svg class="intro" viewBox="0 0 430 285" preserveAspectRatio="none" aria-hidden="true">
    <polygon points="0,20 330,0 430,30 430,285 0,285" fill="var(--blue)"/>
  </svg>

  <div class="brand">
    <div class="brand-mark"></div>
    <div>
      <div class="brand-name">Hollowbrook Rails</div>
      <div class="brand-phone">704-555-0142</div>
      <div class="brand-tag">"Because Good Fences Make Good Neighbors"</div>
    </div>
  </div>

  <div class="intro-text">
    <h1>WE BUILD FENCES....</h1>
    <h2>And we would love to build your fence too!</h2>
    <p>Hollowbrook Rails is a fence installation team that builds new wood &amp; aluminum fences throughout the Braxton NC &amp; surrounding areas. Free Estimates available in person and virtually.</p>
  </div>

  <div class="photo photo-main" role="img" aria-label="Photo of a new wooden privacy fence with gate around a backyard patio"></div>
  <div class="photo photo-rail" role="img" aria-label="Photo of a wood split rail fence with arched gate"></div>
  <div class="photo photo-metal" role="img" aria-label="Photo of a black aluminum fence in a neighborhood yard"></div>
  <div class="photo photo-post" role="img" aria-label="Photo of a wood rail fence with wire mesh beside a house"></div>

  <section class="why">
    <h2>WHY <span>CHOOSE US?</span></h2>
    <p class="lead">Beautiful, professionally installed fences at affordable prices!</p>
    <ul>
      <li><svg viewBox="0 0 10 10"><circle cx="5" cy="5" r="5" fill="var(--blue)"/><path d="M3 5h4M5 3l2 2-2 2" stroke="#fff" stroke-width="1.2" fill="none"/></svg>Free Estimates</li>
      <li><svg viewBox="0 0 10 10"><circle cx="5" cy="5" r="5" fill="var(--blue)"/><path d="M3 5h4M5 3l2 2-2 2" stroke="#fff" stroke-width="1.2" fill="none"/></svg>Professional Installation</li>
      <li><svg viewBox="0 0 10 10"><circle cx="5" cy="5" r="5" fill="var(--blue)"/><path d="M3 5h4M5 3l2 2-2 2" stroke="#fff" stroke-width="1.2" fill="none"/></svg>Concrete in EVERY Post</li>
      <li><svg viewBox="0 0 10 10"><circle cx="5" cy="5" r="5" fill="var(--blue)"/><path d="M3 5h4M5 3l2 2-2 2" stroke="#fff" stroke-width="1.2" fill="none"/></svg>HOA Submission Assistance</li>
      <li><svg viewBox="0 0 10 10"><circle cx="5" cy="5" r="5" fill="var(--blue)"/><path d="M3 5h4M5 3l2 2-2 2" stroke="#fff" stroke-width="1.2" fill="none"/></svg>Lifetime Workmanship Warranty</li>
      <li><svg viewBox="0 0 10 10"><circle cx="5" cy="5" r="5" fill="var(--blue)"/><path d="M3 5h4M5 3l2 2-2 2" stroke="#fff" stroke-width="1.2" fill="none"/></svg>Experienced Installation Teams</li>
      <li><svg viewBox="0 0 10 10"><circle cx="5" cy="5" r="5" fill="var(--blue)"/><path d="M3 5h4M5 3l2 2-2 2" stroke="#fff" stroke-width="1.2" fill="none"/></svg>Quality Workmanship &amp; Materials</li>
      <li><svg viewBox="0 0 10 10"><circle cx="5" cy="5" r="5" fill="var(--blue)"/><path d="M3 5h4M5 3l2 2-2 2" stroke="#fff" stroke-width="1.2" fill="none"/></svg>FREE Gate Adjustments for LIFE</li>
    </ul>
  </section>

  <div class="divider"></div>

  <section class="contact">
    <h2>CONTACT <span>US</span></h2>
    <ul>
      <li><svg viewBox="0 0 36 36"><circle cx="18" cy="18" r="16" fill="var(--blue)" stroke="#fff" stroke-width="2"/><circle cx="18" cy="18" r="11" fill="#fff"/><path d="M18 24s-4-4.5-4-7.5a4 4 0 0 1 8 0c0 3-4 7.5-4 7.5z" fill="var(--blue)"/><circle cx="18" cy="16.5" r="1.4" fill="#fff"/></svg>48 Mill Creek Rd Braxton, NC 28999</li>
      <li><svg viewBox="0 0 36 36"><circle cx="18" cy="18" r="16" fill="var(--blue)" stroke="#fff" stroke-width="2"/><circle cx="18" cy="18" r="11" fill="#fff"/><path d="M14 13.5c.8-.8 1.6-.5 2 .3l.8 1.6c.3.6 0 1.1-.5 1.5-.3.3-.3.6 0 1.1.7 1.1 1.6 2 2.7 2.7.5.3.8.3 1.1 0 .4-.5.9-.8 1.5-.5l1.6.8c.8.4 1.1 1.200.3 2-1.6 1.6-4 .9-6.6-1.6-2.5-2.6-3.3-5.1-2.9-7.9z" fill="var(--blue)"/></svg>704-555-0142</li>
      <li><svg viewBox="0 0 36 36"><circle cx="18" cy="18" r="16" fill="var(--blue)" stroke="#fff" stroke-width="2"/><circle cx="18" cy="18" r="11" fill="#fff"/><rect x="12.5" y="14" width="11" height="8" rx="1" fill="var(--blue)"/><path d="M12.5 14.5l5.5 4 5.5-4" stroke="#fff" stroke-width="1" fill="none"/></svg>office@mybraxtonyard.com</li>
      <li><svg viewBox="0 0 36 36"><circle cx="18" cy="18" r="16" fill="var(--blue)" stroke="#fff" stroke-width="2"/><circle cx="18" cy="18" r="11" fill="#fff"/><circle cx="18" cy="18" r="5.5" fill="none" stroke="var(--blue)" stroke-width="1.4"/><path d="M12.5 18h11M18 12.5c-2.2 3.3-2.2 7.7 0 11M18 12.5c2.2 3.3 2.2 7.7 0 11" stroke="var(--blue)" stroke-width="1.1" fill="none"/></svg>www.MyBraxtonYard.com</li>
    </ul>
  </section>

  <footer class="footer">
    <p class="verse">“I AM WITH YOU ALWAYS”</p>
    <p class="ref">MATTHEW 28:20</p>
  </footer>
</main>
</body>
</html>
```